Start-up braucht modernes/hochwertiges Getränkeetikett
Zielgruppe
Wir sind ein modernes, nachhaltiges Start-up, welches eine neue Getränkekategorie auf den Markt bringt. Ein sogenanntes Elektrolyt-Getränk mit dem Namen KLORV5. Es ist abgefüllt in eine 500 ml Flasche und enthält Magnesium, Kalzium, Kalium, und Natrium. Diese Stoffe (Elektrolyte) dienen der körperlichen Hydrierung. Zu Dehydrierung kann es durch Hitze, Alkohol, Sport oder Krankheit kommen. Krankheit liegt bei uns allerdings nicht im Fokus. In unserer Zielgruppe befinden sich hauptsächlich Personen im Alter von 18 - 29 Jahren.
Die Geschmacksrichtung ist Zitrone-Limette.
Aufgabenstellung
Das Etikett soll:
- MODERN, SCHLICHT und HOCHWERTIG sein, so dass es im Supermarkt hervorsticht
- erkenntlich machen, dass die Stoffe Magnesium, Natrium, Kalzium und Kalium enthalten sind
- sich farblich deutlich von der Farbe des Inhalts (weiß) abheben. (Vorzugsweise mit einem hellen Blau, türkis)
- für unsere junge Zielgruppe ansprechend sein
- ebenfalls auf die Geschmacksrichtung (Zitrone-Limette) hinweisen, und zwar so, dass wenn man eine weitere Geschmacksrichtung auf den Markt bringen möchte, diese leicht angepasst werden kann.
- nicht nach einem Energydrink oder einem typischen Sportgetränk aussehen
- unter dem Namen den Slogan 'Elektrolyt-Getränk' stehen haben
-Das Etikett ist nicht dursichtig sondern besteht aus Papier
Der Name sowie das Logo können selbstverständlich farblich verändert werden. Bei dem Logo können auch größere Änderungen vollzogen werden.
Bitte beachten Sie die unten zu stehenden Regler um sich einen guten Überblick über unsere Vorstellungen zu verschaffen. Die Platzierung des EAN-Code ist für ihr Design irrelevat .
Bei Unklarheiten gerne nachfragen!

```html
<!DOCTYPE html>
<html lang="de">
<head>
<meta charset="utf-8">
<title>KLORV5 – Elektrolyt-Getränk</title>
<link rel="stylesheet" href="https://fonts.googleapis.com/css2?family=Roboto+Slab:wght@300;700&display=swap">
<style>
  :root {
    --bg: #c2e4ea;
    --bg-swirl: #b3dce4;
    --ink: #161616;
    --rule: #ffffff;
    --flavour-mark: #c4d65a;
  }
  * { margin: 0; padding: 0; box-sizing: border-box; }
  html, body { width: 1200px; height: 523px; overflow: hidden; }
  body {
    position: relative;
    font-family: "Roboto Slab", Georgia, serif;
    color: var(--ink);
    background: var(--bg);
  }
  .backdrop {
    position: absolute; inset: 0;
    background:
      radial-gradient(ellipse 260px 120px at 180px 140px, var(--bg-swirl), transparent 70%),
      radial-gradient(ellipse 300px 140px at 1020px 380px, var(--bg-swirl), transparent 70%),
      radial-gradient(ellipse 220px 110px at 300px 430px, var(--bg-swirl), transparent 70%),
      var(--bg);
  }
  .brand-ring {
    position: absolute; left: 602px; top: 33px;
    width: 78px; height: 78px;
    border: 2px solid var(--ink); border-radius: 50%;
  }
  .brand-name {
    position: absolute; left: 0; width: 1282px; top: 126px;
    text-align: center; font-weight: 700; font-size: 47px;
    letter-spacing: 1px; line-height: 1;
  }
  .facts {
    position: absolute; left: 421px; top: 208px;
    width: 441px; height: 259px;
    border: 2px solid var(--rule);
  }
  .facts .rule-h, .facts .rule-v { position: absolute; background: var(--rule); }
  .rule-h.one { left: 0; right: 0; top: 68px; height: 2px; }
  .rule-h.two { left: 0; right: 0; top: 116px; height: 2px; }
  .rule-v { left: 217px; width: 2px; top: 68px; bottom: 0; }
  .subtitle {
    position: absolute; left: 0; right: 0; top: 17px;
    text-align: center; font-weight: 700; font-size: 30px; line-height: 1.2;
  }
  .label {
    position: absolute; left: 43px; font-weight: 700; font-size: 21px; line-height: 25.5px;
  }
  .label.flavour { top: 77px; }
  .label.ingredients { top: 134px; }
  .value {
    position: absolute; left: 250px; font-weight: 300; font-size: 23px; line-height: 25.8px;
  }
  .value.flavour { top: 75px; }
  .flavour-mark {
    position: absolute; left: 234px; top: 77px; width: 181px; height: 30px;
  }
  .value.ingredients { top: 133px; list-style: none; }
</style>
</head>
<body>
  <div class="backdrop" role="img" aria-label="Marmoriertes Wirbelmuster in hellem Türkis"></div>

  <div class="brand-ring"></div>
  <h1 class="brand-name">KLORV5</h1>

  <section class="facts">
    <h2 class="subtitle">Elektrolyt-Getränk</h2>
    <div class="rule-h one"></div>
    <div class="rule-h two"></div>
    <div class="rule-v"></div>

    <p class="label flavour">Geschmack:</p>
    <svg class="flavour-mark" viewBox="0 0 181 30" aria-hidden="true">
      <polygon points="6,2 181,0 176,29 0,30" fill="var(--flavour-mark)"/>
    </svg>
    <p class="value flavour">Zitrone-Limette</p>

    <p class="label ingredients">Inhaltstoffe<br>die dich fit<br>halten:</p>
    <ul class="value ingredients">
      <li>+ Magnesium</li>
      <li>+ Natrium</li>
      <li>+ Kalzium</li>
      <li>+ Kalium</li>
    </ul>
  </section>
</body>
</html>
```